EmberGuard Larkton- Making Larkton A Wildfire Adapted Community

Design a two complimentary graphics with text that can be used for a banner and "mini-billboard" to promote the project and encourage citizens to go to the webpage to learn more. Using the attached document as examples of what we want the two banners to say.
The goal of EmberGuard Larkton is to plan and prepare so if an urban wildfire occurs, catastrophic loss can be avoided. EmberGuard Larkton focuses on reducing the risk of and catastrophic losses to resources and private property on private land in Larkton, MT. Property owners are encouraged to be proactive to address hazardous fuel conditions on their property, reduce structure ignition potential within their home ignition zone and employ wildfire resilient principles to sustain a fire adapted home, property and community. Ember showers from a wildfire next to the city is the biggest concern.

Target Market(s)

Residents in the project area of Larkton. Signs and banners will be displayed on public lands and private yeards

Font styles to use
Sans Serif

Requirements
Must have
• Graphics, use of the ValleyRidge Ember Watch Council logo. Must incorporate the text that is part of the attachment.
Nice to have
• Get people's attention. A simple graphic that get's people's attention.
Should not have
• small details.

```html
<!DOCTYPE html>
<html lang="en">
<head>
<meta charset="utf-8">
<title>EmberGuard Larkton – Prepare Now Banner</title>
<link href="https://fonts.googleapis.com/css2?family=Arimo:wght@700&display=swap" rel="stylesheet">
<style>
  :root {
    --panel-bg: #dde190;
    --brand-green: #238a17;
    --edge-lime: #62e01c;
    --sky-top: #6e1a0c;
    --sky-mid: #c24a12;
    --sky-glow: #f39a1e;
    --ground: #1b1010;
    --caption-box: rgba(0, 0, 0, 0.82);
    --white: #ffffff;
  }
  * { margin: 0; padding: 0; box-sizing: border-box; }
  html, body { width: 1200px; height: 402px; overflow: hidden; background: var(--panel-bg); }
  .banner {
    position: relative;
    width: 1200px;
    height: 402px;
    background: var(--panel-bg);
    font-family: "Arimo", Arial, sans-serif;
    font-weight: 700;
    overflow: hidden;
  }
  .fire-scene {
    position: absolute;
    inset: 0;
    width: 1200px;
    height: 402px;
  }
  .warning-caption {
    position: absolute;
    left: 75px;
    top: 86px;
    width: 173px;
    height: 220px;
    background: var(--caption-box);
    color: var(--white);
    font-size: 19.5px;
    line-height: 1.2;
    text-align: center;
    display: flex;
    align-items: center;
    justify-content: center;
  }
  .message {
    position: absolute;
    left: 640px;
    width: 575px;
    text-align: center;
    color: var(--brand-green);
  }
  .headline {
    top: 30px;
    font-size: 38px;
    line-height: 1.12;
  }
  .council-name {
    top: 190px;
    font-size: 22px;
    line-height: 1.25;
    display: flex;
    align-items: center;
    justify-content: center;
    gap: 14px;
  }
  .council-name .mark {
    width: 22px;
    height: 22px;
    border-radius: 50%;
    background: var(--brand-green);
    flex: none;
  }
  .learn-more {
    top: 330px;
    font-size: 19.5px;
  }
  .web-address {
    top: 358px;
    font-size: 21px;
    letter-spacing: 2px;
  }
</style>
</head>
<body>
  <main class="banner">
    <svg class="fire-scene" viewBox="0 0 1200 402" aria-hidden="false">
      <defs>
        <linearGradient id="fireSky" x1="0" y1="0" x2="0" y2="1">
          <stop offset="0" stop-color="var(--sky-top)"/>
          <stop offset="0.45" stop-color="var(--sky-mid)"/>
          <stop offset="0.72" stop-color="var(--sky-glow)"/>
          <stop offset="0.8" stop-color="var(--ground)"/>
          <stop offset="1" stop-color="var(--ground)"/>
        </linearGradient>
      </defs>
      <path d="M0,0 H330 C420,0 460,70 515,170 C575,285 640,385 735,402 H0 Z"
            fill="none" stroke="var(--edge-lime)" stroke-width="10" transform="translate(6,0)"/>
      <path role="img" aria-label="Silhouetted forest and houses in front of a wildfire glowing orange under a dark red sky with birds flying"
            d="M0,0 H330 C420,0 460,70 515,170 C575,285 640,385 735,402 H0 Z"
            fill="url(#fireSky)"/>
    </svg>

    <div class="warning-caption">
      <p>You<br>DO NOT<br>Have to<br>LIVE IN<br>A FOREST<br>to be in a<br>WILDFIRE!</p>
    </div>

    <h1 class="message headline">PREPARE NOW!<br>Your home... Your loss...<br>YOUR CHOICE!</h1>

    <p class="message council-name"><span class="mark"></span><span>ValleyRidge Ember<br>Watch Council</span></p>

    <p class="message learn-more">Learn more at EMBERGUARD LARKTON</p>
    <p class="message web-address">WWW.VREWC.ORG</p>
  </main>
</body>
</html>
```